Startup Drone Platform Company business card

We are needing a business card design for our employees. We are a startup drone platform. We are looking for a business card that has our logo on one side, with the employee/company details on the opposite side. We are looking for something that is very eye catching, modern, and bold.

Target Market(s)

This will target both drone pilots and drone businesses, along with all the industries that could utilize drone services (aerial video, aerial photos, inspections, 3d mapping, etc).

Industry/Entity Type

Business

```html
<!DOCTYPE html>
<html lang="en">
<head>
<meta charset="utf-8">
<title>Skylift Rentals – Business Card</title>
<link href="https://fonts.googleapis.com/css2?family=Lato:wght@400;700;900&family=Open+Sans:wght@400&display=swap" rel="stylesheet">
<style>
  :root {
    --teal: #3bb6c4;
    --teal-light: #bfe6ea;
    --black: #050505;
    --white: #ffffff;
    --ink: #3a3a3a;
    --grey: #a9a9a9;
    --backdrop: #e9e6e2;
  }
  * { margin: 0; padding: 0; box-sizing: border-box; }
  html, body { width: 1200px; height: 900px; overflow: hidden; }
  body {
    background: var(--backdrop);
    position: relative;
    font-family: "Open Sans", sans-serif;
  }
  .card {
    position: absolute;
    left: 290px;
    width: 620px;
    height: 354px;
    overflow: hidden;
    box-shadow: 0 10px 28px rgba(0,0,0,0.18);
  }
  /* Front side */
  .card-front { top: 60px; background: var(--black); }
  .card-front .band {
    position: absolute; left: 0; right: 0; bottom: 0; height: 56px;
    background: linear-gradient(90deg, #0d1b1d 0%, #1f5a60 55%, var(--teal) 100%);
  }
  .brand {
    position: absolute; left: 0; right: 0; top: 118px;
    display: flex; flex-direction: column; align-items: center; gap: 18px;
  }
  .brand-dot {
    width: 46px; height: 46px; border-radius: 50%;
    background: var(--teal);
  }
  .brand-name {
    font-family: "Lato", sans-serif; font-weight: 400;
    font-size: 30px; letter-spacing: 12px; color: var(--white);
    padding-left: 12px;
  }
  /* Back side */
  .card-back { top: 486px; background: var(--white); }
  .card-back .band {
    position: absolute; left: 0; right: 0; bottom: 0; height: 58px;
    background: linear-gradient(90deg, #ffffff 25%, var(--teal-light) 60%, var(--teal) 100%);
  }
  .deco-ring {
    position: absolute; right: -40px; top: 40px;
    width: 230px; height: 230px; border-radius: 50%;
    border: 8px solid #d6eef1;
  }
  .details { position: absolute; left: 46px; top: 56px; color: var(--ink); }
  .person-name {
    font-family: "Lato", sans-serif; font-weight: 900;
    font-size: 34px; color: var(--teal); line-height: 1; letter-spacing: -0.5px;
  }
  .person-role {
    font-family: "Lato", sans-serif; font-weight: 700;
    font-size: 13px; color: var(--teal); margin-left: 60px; margin-top: 2px;
  }
  .address { margin-top: 26px; font-size: 15px; line-height: 1.35; }
  .contacts { list-style: none; margin-top: 20px; font-size: 14px; line-height: 1.5; }
  .contacts li { display: flex; align-items: center; gap: 8px; }
  .contacts svg { width: 18px; height: 18px; fill: none; stroke: var(--teal); stroke-width: 1.8; }
</style>
</head>
<body>
  <section class="card card-front" aria-label="Card front">
    <div class="brand">
      <span class="brand-dot"></span>
      <span class="brand-name">SKYLIFT RENTALS</span>
    </div>
    <div class="band"></div>
  </section>

  <section class="card card-back" aria-label="Card back">
    <div class="deco-ring"></div>
    <div class="details">
      <h1 class="person-name">YOUR NAME</h1>
      <p class="person-role">POSITION</p>
      <p class="address">PO BOX 1234, Address Line 1,<br>Address Line 2,<br>Address Line 3</p>
      <ul class="contacts">
        <li><svg viewBox="0 0 24 24"><path d="M5 4h4l2 5-3 2a11 11 0 0 0 5 5l2-3 5 2v4a2 2 0 0 1-2 2A16 16 0 0 1 3 6a2 2 0 0 1 2-2z"/></svg>123-456-7890</li>
        <li><svg viewBox="0 0 24 24"><rect x="6" y="3" width="12" height="6"/><rect x="3" y="9" width="18" height="8" rx="1"/><rect x="6" y="14" width="12" height="7"/></svg>123-456-7890</li>
        <li><svg viewBox="0 0 24 24"><rect x="3" y="5" width="18" height="14"/><path d="M3 5l9 8 9-8"/></svg>youremail@example.com</li>
        <li><svg viewBox="0 0 24 24"><circle cx="12" cy="12" r="9"/><path d="M3 12h18M12 3c3 3 3 15 0 18M12 3c-3 3-3 15 0 18"/></svg>www.website.com</li>
      </ul>
    </div>
    <div class="band"></div>
  </section>
</body>
</html>
```